New corporate Powerpoint template *

Hi,
We would like to have one new corporate Powerpoint template which can be used for various presentations (Sales, Investors, Marketing, Engineers, HR, Corporate presentations…) Please note that this template will be used for both internal and external presentations.
Please take a look at our website to get a feel for our branding.
https://www.vemtra-microdevices.example/

Some visual elements to include:

• The theme needs to be relevant to our industry i.e. Semiconductor theme (circuit board/chip graphic elements)
• Simple uses of color, lifestyle images, moving away from Geometric patterns and colorful wave
• Style should be modern, clean and gender neutral
• Use Vemtra blue as more of an accent color - Avoid the overuse of blue (seems a little too bright sometimes)
• Vemtra logo to appear on every page

Necessary slides to include:
• Cover Slide
• Agenda Slide
• Divider / Title Slide
• Content Slide
• White Slide
• Comparison slide (two, three, four)
• Table slide with the ability to add rows/columns
• Timeline/roadmap slide
• End Slide

Target Market(s)

Semiconductor industry

Font styles to use
Other font styles liked:
• Arial or Rockwell

Colors
33a6d7

Requirements
Must have
• • The theme needs to be relevant to our industry i.e. Semiconductor theme (circuit board/chip graphic elements)
• • Simple uses of color, lifestyle images
• • Style should be modern, clean and gender neutral
• • Use Vemtra blue as more of an accent color
• • Vemtra logo to appear on every page
• Necessary slides to include:
• • Cover Slide
• • Agenda Slide
• • Divider / Title Slide
• • Content Slide
• • White Slide
• • Comparison slide (two, three, four)
• • Table slide with the ability to add rows/columns
• • Timeline/roadmap slide
• • End Slide
Should not have
• - Avoid the overuse of blue (seems a little too bright sometimes)
• - Do not use any kind of wave as a graphic

```html
<!DOCTYPE html>
<html lang="en">
<head>
<meta charset="utf-8">
<title>Vemtra corporate presentation template</title>
<link rel="stylesheet" href="https://fonts.googleapis.com/css2?family=Lato:wght@300;400;700;900&display=swap">
<style>
:root{
  --stage:#5b6e80;
  --blue:#1f74bb;
  --sky:#33a6d7;
  --navy:#2c3e50;
  --yellow:#f2c318;
  --orange:#f08a2c;
  --green:#3bb54a;
  --ink:#333;
  --soft:#8a8f96;
  --line:#e3e6ea;
}
*{box-sizing:border-box;margin:0;padding:0}
html,body{width:1200px;height:1200px;overflow:hidden}
body{background:var(--stage);font-family:'Lato',Arial,sans-serif;color:var(--ink);position:relative}
.slide{position:absolute;width:288px;height:161px;background:#fff;overflow:hidden}
.c1{left:14px}.c2{left:310px}.c3{left:606px}.c4{left:902px}
.r1{top:56px}.r2{top:243px}.r3{top:430px}.r4{top:617px}.r5{top:804px}.r6{top:991px}
.abs{position:absolute}
.foot{position:absolute;left:0;right:0;bottom:0;height:3px;background:linear-gradient(90deg,var(--blue) 0 55%,var(--green) 55%)}
.tag{position:absolute;right:4px;bottom:3px;background:var(--blue);color:#fff;font-size:4.5px;font-weight:700;padding:1px 4px;border-radius:2px 2px 0 0}
.ttl{position:absolute;top:8px;left:0;width:100%;text-align:center;font-size:8.5px;font-weight:700;color:var(--ink)}
.sub{position:absolute;top:25px;left:0;width:100%;text-align:center;font-size:3.6px;color:var(--soft)}
.bars{position:absolute;top:20px;left:50%;transform:translateX(-50%);display:flex;gap:1.5px}
.bars i{display:block;width:7px;height:1.5px}
.fine{font-size:3.5px;line-height:1.45;color:#6d737a}
.fine b{color:var(--ink)}
.photo{position:absolute}
.pill{position:absolute;height:6px;border-radius:3px;color:#fff;font-size:4.2px;font-weight:700;text-align:center;line-height:6px}
.note{position:absolute;font-size:3.1px;line-height:1.4;color:var(--soft);text-align:center}
.big{font-weight:900}
.cols{position:absolute;display:grid;gap:10px}
.card{position:absolute;background:#fff;box-shadow:0 0 3px rgba(0,0,0,.18)}
.card .rec{height:4px;font-size:2.6px;letter-spacing:.4px;color:#fff;text-align:center;line-height:4px}
.card .pkg{font-size:5px;padding:3px 4px 0}
.card .price{font-size:3.2px;color:var(--soft);padding:1px 4px 3px;border-bottom:.5px solid var(--line)}
.card ul{list-style:none;padding:2px 4px;font-size:2.9px;line-height:2;color:#555}
.card li::before{content:"✓ ";color:var(--ink)}
.card .try{position:absolute;left:0;right:0;bottom:0;height:6px;color:#fff;font-size:3px;text-align:center;line-height:6px}
table.grid{border-collapse:collapse;width:100%;font-size:3px;color:var(--soft)}
table.grid th{background:var(--blue);color:#fff;font-weight:400;padding:1.5px 2px;text-align:left}
table.grid td{padding:3px 2px;border-bottom:.5px solid var(--line)}
</style>
</head>
<body>

<!-- Row 1 -->
<section class="slide c1 r1">
  <div class="photo" role="img" aria-label="Office desk with computer" style="left:0;top:0;width:205px;height:95px;background:linear-gradient(135deg,#cfd6dd,#f3f5f7 60%,#b9c2cb);clip-path:polygon(0 0,100% 0,62% 100%,0 100%)"></div>
  <div class="photo" role="img" aria-label="Chip on a blue hexagon circuit pattern" style="left:0;top:92px;width:185px;height:69px;background:linear-gradient(120deg,#4f8fc0,#7fb4da 55%,#d0913a);clip-path:polygon(0 0,78% 0,100% 100%,0 100%)"></div>
  <div class="abs" style="left:183px;top:98px;display:flex;align-items:center;gap:3px">
    <span style="width:9px;height:9px;border-radius:50%;background:var(--sky);display:block"></span>
    <span style="font-size:14px;font-weight:700;color:var(--blue)">Vemtra</span>
  </div>
  <div class="foot"></div><div class="tag">Vemtra</div>
</section>

<section class="slide c2 r1">
  <div class="ttl">Lorem ipsum dolor</div>
  <div class="photo" role="img" aria-label="Chip on a blue hexagon circuit pattern" style="left:0;top:34px;width:288px;height:56px;background:linear-gradient(100deg,#5d9ccc,#8fc0e2 45%,#c7923e 60%,#6aa5d2)"></div>
  <div class="cols fine" style="left:20px;top:100px;width:248px;grid-template-columns:1fr 1fr">
    <p><b>Lorem ipsum dolor sit amet,</b> short notes on the key point for this slide go here with a brief line of support text. Keep each line clear and simple for the reader.</p>
    <p>Lorem ipsum dolor sit amet, short notes on the key point for this slide go here with a brief line of support text. Keep each line clear and simple for the reader.</p>
  </div>
  <div class="foot"></div><div class="tag">Vemtra</div>
</section>

<section class="slide c3 r1">
  <div class="ttl">Lorem ipsum dolor</div>
  <div class="photo" role="img" aria-label="Circuit board close-up" style="left:0;top:38px;width:140px;height:42px;border-radius:0 10px 10px 0;background:linear-gradient(110deg,#4b4f6b,#8a7d9a 50%,#2b66b0)"></div>
  <div class="abs fine" style="left:160px;top:44px;width:110px">
    <p style="display:flex;gap:3px;margin-bottom:6px"><span style="color:var(--blue);font-size:6px">✔</span><span>Short note on the key point for this slide here.</span></p>
    <p style="display:flex;gap:3px"><span style="color:var(--blue);font-size:6px">✔</span><span>Short note on the key point for this slide here.</span></p>
  </div>
  <div class="abs fine" style="left:12px;top:95px;width:135px"><b>Lorem ipsum dolor sit amet,</b> short notes on the key point for this slide go here with a brief line of support text for the reader.</div>
  <div class="photo" role="img" aria-label="Dark circuit board close-up" style="left:150px;top:94px;width:138px;height:50px;border-radius:10px 0 0 10px;background:linear-gradient(120deg,#2c3340,#5a6270 50%,#23282f)"></div>
  <div class="foot"></div><div class="tag">Vemtra</div>
</section>

<section class="slide c4 r1">
  <div class="ttl">Growth</div>
  <div class="photo" role="img" aria-label="Hand drawing a rising bar chart with doodle icons" style="left:10px;top:30px;width:140px;height:120px;background:radial-gradient(circle at 55% 45%,#fbe7d8,#f4f6f8 65%,#fff)"></div>
  <div class="abs" style="left:158px;top:98px;width:26px;height:12px;background:var(--blue);color:#fff;font-size:5px;font-weight:700;text-align:center;line-height:12px">Step 1</div>
  <div class="abs" style="left:178px;top:74px;width:26px;height:12px;background:var(--yellow);color:#fff;font-size:5px;font-weight:700;text-align:center;line-height:12px">Step 2</div>
  <div class="abs" style="left:198px;top:50px;width:26px;height:12px;background:var(--navy);color:#fff;font-size:5px;font-weight:700;text-align:center;line-height:12px">Step 3</div>
  <div class="abs fine" style="left:188px;top:98px;width:40px"><b>INFORMATION</b><br>Short note here.</div>
  <div class="abs fine" style="left:208px;top:74px;width:40px"><b>INFORMATION</b><br>Short note here.</div>
  <div class="abs fine" style="left:228px;top:50px;width:40px"><b>INFORMATION</b><br>Short note here.</div>
  <div class="foot"></div><div class="tag">Vemtra</div>
</section>

<!-- Row 2 -->
<section class="slide c1 r2">
  <div class="ttl">Text One Column</div>
  <div class="abs fine" style="left:28px;top:38px;width:232px">
    <p style="margin-bottom:4px"><b>Lorem ipsum dolor</b> sit amet, short notes on the key point for this slide go here with a brief line of support text. Keep each line clear and simple for the reader and the room.</p>
    <p style="margin-bottom:4px"><b>Aliquam et ante nunc</b> short notes on the key point for this slide go here with a brief line of support text. Keep each line clear and simple for the reader and the room.</p>
    <p style="margin-bottom:4px">Donec vitae dolor sed urna laoreet short notes on the key point for this slide go here.</p>
    <p>Fusce tincidunt eget ligula short notes on the key point for this slide go here.</p>
  </div>
  <div class="foot"></div><div class="tag">Vemtra</div>
</section>

<section class="slide c2 r2">
  <div class="ttl">Text Two Column</div>
  <div class="bars"><i style="background:var(--blue)"></i><i style="background:var(--navy)"></i><i style="background:var(--yellow)"></i><i style="background:var(--orange)"></i></div>
  <div class="sub">Your great subtitle in this line</div>
  <div class="cols fine" style="left:26px;top:38px;width:236px;grid-template-columns:1fr 1fr">
    <p><b>Lorem ipsum dolor</b> sit amet, short notes on the key point for this slide go here with a brief line of support text. Keep each line clear and simple for the reader.<br><br><b>Quisque sed ex nec</b> short notes on the key point for this slide go here.<br><br>Aliquam et ante nunc short notes on the key point.</p>
    <p>Et diam. Short notes on the key point for this slide go here with a brief line of support text. Keep each line clear and simple for the reader.<br><br>Donec vitae dolor short notes on the key point for this slide go here.<br><br>Fusce tincidunt short notes on the key point.</p>
  </div>
  <div class="foot"></div><div class="tag">Vemtra</div>
</section>

<section class="slide c3 r2">
  <div class="ttl">Text Three Column</div>
  <div class="bars"><i style="background:var(--blue)"></i><i style="background:var(--navy)"></i><i style="background:var(--yellow)"></i><i style="background:var(--orange)"></i></div>
  <div class="sub">Your great subtitle in this line</div>
  <div class="cols fine" style="left:26px;top:38px;width:236px;grid-template-columns:1fr 1fr 1fr;gap:8px">
    <p><b>Lorem ipsum dolor</b> sit amet, short notes on the key point for this slide go here with a line of support.<br><br><b>Quisque sed ex</b> short notes on the key point.</p>
    <p>Aliquam et ante nunc short notes on the key point for this slide go here with a line of support.<br><br>Donec eget short notes on the key point.</p>
    <p>Luctus dapibus short notes on the key point for this slide go here with a line of support.<br><br>Fusce tincidunt short notes on the key point.</p>
  </div>
  <div class="foot"></div><div class="tag">Vemtra</div>
</section>

<section class="slide c4 r2">
  <div class="ttl">Company Timeline</div>
  <svg class="abs" style="left:0;top:0" width="288" height="161" viewBox="0 0 288 161">
    <line x1="20" y1="100" x2="268" y2="100" stroke="#cfd4da" stroke-width="1"/>
    <g font-family="Lato,Arial,sans-serif" font-weight="900" font-size="7" text-anchor="middle">
      <line x1="50" y1="55" x2="50" y2="100" stroke="var(--blue)" stroke-width="1.5"/><circle cx="50" cy="48" r="10" fill="var(--blue)"/><circle cx="50" cy="48" r="4" fill="none" stroke="#fff"/>
      <text x="50" y="114" fill="var(--blue)">1980</text>
      <line x1="103" y1="100" x2="103" y2="124" stroke="var(--navy)" stroke-width="1.5"/><circle cx="103" cy="126" r="9" fill="var(--navy)"/><circle cx="103" cy="126" r="3.5" fill="none" stroke="#fff"/>
      <text x="103" y="146" fill="var(--navy)">1990</text>
      <line x1="156" y1="55" x2="156" y2="100" stroke="var(--yellow)" stroke-width="1.5"/><circle cx="156" cy="48" r="10" fill="var(--yellow)"/><rect x="152" y="45" width="8" height="5" fill="none" stroke="#fff"/>
      <text x="156" y="114" fill="var(--yellow)">2000</text>
      <line x1="209" y1="100" x2="209" y2="124" stroke="var(--orange)" stroke-width="1.5"/><circle cx="209" cy="126" r="9" fill="var(--orange)"/><path d="M205 122h8l-8 8h8z" fill="none" stroke="#fff"/>
      <text x="209" y="146" fill="var(--orange)">2010</text>
      <line x1="262" y1="55" x2="262" y2="100" stroke="var(--blue)" stroke-width="1.5"/><circle cx="262" cy="48" r="10" fill="var(--blue)"/><path d="M258 44h8l-4 6z" fill="none" stroke="#fff"/>
      <text x="262" y="114" fill="var(--blue)">2020</text>
    </g>
  </svg>
  <div class="note" style="left:36px;top:116px;width:28px">Short note here.</div>
  <div class="note" style="left:142px;top:116px;width:28px">Short note here.</div>
  <div class="note" style="left:248px;top:116px;width:28px">Short note here.</div>
  <div class="foot"></div><div class="tag">Vemtra</div>
</section>

<!-- Row 3 -->
<section class="slide c1 r3">
  <div class="ttl">Info graphics</div>
  <svg class="abs" style="left:104px;top:36px" width="80" height="110" viewBox="0 0 80 80">
    <g fill="none" stroke-width="16" transform="rotate(-90 40 40)">
      <circle cx="40" cy="40" r="30" stroke="var(--blue)" stroke-dasharray="29 159.5" stroke-dashoffset="0"/>
      <circle cx="40" cy="40" r="30" stroke="var(--yellow)" stroke-dasharray="29 159.5" stroke-dashoffset="-31.4"/>
      <circle cx="40" cy="40" r="30" stroke="var(--blue)" stroke-dasharray="29 159.5" stroke-dashoffset="-62.8"/>
      <circle cx="40" cy="40" r="30" stroke="var(--navy)" stroke-dasharray="29 159.5" stroke-dashoffset="-94.2"/>
      <circle cx="40" cy="40" r="30" stroke="var(--orange)" stroke-dasharray="29 159.5" stroke-dashoffset="-125.6"/>
      <circle cx="40" cy="40" r="30" stroke="var(--blue)" stroke-dasharray="29 159.5" stroke-dashoffset="-157"/>
    </g>
    <circle cx="40" cy="40" r="19" fill="var(--blue)"/>
    <text x="40" y="39" fill="#fff" font-family="Lato,Arial,sans-serif" font-size="6" font-weight="700" text-anchor="middle">100%</text>
    <text x="40" y="45" fill="#fff" font-family="Lato,Arial,sans-serif" font-size="2.6" text-anchor="middle">Short note here</text>
  </svg>
  <div class="pill" style="left:54px;top:40px;width:36px;background:var(--navy)">Data</div>
  <div class="note" style="left:54px;top:48px;width:36px">Short note on this point here.</div>
  <div class="pill" style="left:54px;top:74px;width:36px;background:var(--blue)">Data</div>
  <div class="note" style="left:54px;top:82px;width:36px">Short note on this point here.</div>
  <div class="pill" style="left:54px;top:108px;width:36px;background:var(--orange)">Data</div>
  <div class="note" style="left:54px;top:116px;width:36px">Short note on this point here.</div>
  <div class="pill" style="left:198px;top:40px;width:36px;background:var(--blue)">Data</div>
  <div class="note" style="left:198px;top:48px;width:36px">Short note on this point here.</div>
  <div class="pill" style="left:198px;top:74px;width:36px;background:var(--yellow)">Data</div>
  <div class="note" style="left:198px;top:82px;width:36px">Short note on this point here.</div>
  <div class="pill" style="left:198px;top:108px;width:36px;background:var(--blue)">Data</div>
  <div class="note" style="left:198px;top:116px;width:36px">Short note on this point here.</div>
  <div class="foot"></div><div class="tag">Vemtra</div>
</section>

<section class="slide c2 r3">
  <div class="ttl">Laptop</div>
  <div class="abs" style="left:92px;top:34px;width:104px;height:68px;background:#1f2328;border-radius:3px;padding:3px">
    <div style="width:100%;height:100%;background:linear-gradient(135deg,#27b0a0,#5fd0b8);color:#fff;padding:4px 5px">
      <div style="font-size:4.5px;font-weight:700">Information</div>
      <div style="font-size:13px;font-weight:900;line-height:1.1">74%</div>
      <div style="font-size:2.8px;line-height:1.4">Short note on the key point for this slide goes here with a line of support text for the reader.</div>
    </div>
  </div>
  <div class="abs" style="left:82px;top:101px;width:124px;height:3px;background:#c9cdd2;border-radius:0 0 2px 2px"></div>
  <div class="abs" style="left:0;top:106px;width:288px;height:55px;background:var(--blue)"></div>
  <div class="abs" style="left:20px;top:120px;width:250px;display:grid;grid-template-columns:1fr 1fr 1fr;gap:10px;color:#fff;font-size:3.2px;line-height:1.4">
    <p style="display:flex;gap:3px"><span style="font-size:6px">✔</span><span>Short note on the key point for this slide here.</span></p>
    <p style="display:flex;gap:3px"><span style="font-size:6px">✔</span><span>Short note on the key point for this slide here.</span></p>
    <p style="display:flex;gap:3px"><span style="font-size:6px">✔</span><span>Short note on the key point for this slide here.</span></p>
  </div>
  <div class="tag" style="bottom:0;background:#fff;color:var(--blue)">Vemtra</div>
</section>

<section class="slide c3 r3">
  <div class="ttl">Circle Info</div>
  <svg class="abs" style="left:104px;top:38px" width="80" height="80" viewBox="0 0 80 80">
    <g fill="none" stroke-width="20" transform="rotate(-90 40 40)">
      <circle cx="40" cy="40" r="28" stroke="var(--blue)" stroke-dasharray="27 148.9" stroke-dashoffset="0"/>
      <circle cx="40" cy="40" r="28" stroke="var(--yellow)" stroke-dasharray="27 148.9" stroke-dashoffset="-29.3"/>
      <circle cx="40" cy="40" r="28" stroke="var(--navy)" stroke-dasharray="27 148.9" stroke-dashoffset="-58.6"/>
      <circle cx="40" cy="40" r="28" stroke="var(--orange)" stroke-dasharray="27 148.9" stroke-dashoffset="-87.9"/>
      <circle cx="40" cy="40" r="28" stroke="var(--blue)" stroke-dasharray="27 148.9" stroke-dashoffset="-117.2"/>
      <circle cx="40" cy="40" r="28" stroke="var(--blue)" stroke-dasharray="27 148.9" stroke-dashoffset="-146.5"/>
    </g>
    <text x="40" y="40" fill="var(--yellow)" font-family="Lato,Arial,sans-serif" font-size="4.5" font-weight="700" text-anchor="middle">Data Here</text>
    <text x="40" y="45" fill="#999" font-family="Lato,Arial,sans-serif" font-size="2.4" text-anchor="middle">Short note here</text>
  </svg>
  <div class="pill" style="left:54px;top:44px;width:36px;background:var(--blue)">Data</div>
  <div class="note" style="left:54px;top:52px;width:36px">Short note on this point here.</div>
  <div class="pill" style="left:54px;top:76px;width:36px;background:var(--blue)">Data</div>
  <div class="note" style="left:54px;top:84px;width:36px">Short note on this point here.</div>
  <div class="pill" style="left:54px;top:108px;width:36px;background:var(--blue)">Data</div>
  <div class="note" style="left:54px;top:116px;width:36px">Short note on this point here.</div>
  <div class="pill" style="left:198px;top:44px;width:36px;background:var(--yellow)">Data</div>
  <div class="note" style="left:198px;top:52px;width:36px">Short note on this point here.</div>
  <div class="pill" style="left:198px;top:76px;width:36px;background:var(--navy)">Data</div>
  <div class="note" style="left:198px;top:84px;width:36px">Short note on this point here.</div>
  <div class="pill" style="left:198px;top:108px;width:36px;background:var(--orange)">Data</div>
  <div class="note" style="left:198px;top:116px;width:36px">Short note on this point here.</div>
  <div class="foot"></div><div class="tag">Vemtra</div>
</section>

<section class="slide c4 r3">
  <div class="ttl">Map Of The World</div>
  <div class="photo" role="img" aria-label="Grey world map with highlighted countries" style="left:66px;top:36px;width:156px;height:76px;background:radial-gradient(ellipse at 50% 50%,#d5d9de,#eef0f2 70%,#fff)"></div>
  <div class="pill" style="left:14px;top:60px;width:40px;background:var(--yellow)">Investment</div>
  <div class="note" style="left:14px;top:68px;width:40px">Short note on this point.</div>
  <div class="pill" style="left:40px;top:96px;width:36px;background:var(--navy)">Ecology</div>
  <div class="pill" style="left:232px;top:34px;width:42px;background:var(--blue)">Industry</div>
  <div class="note" style="left:232px;top:42px;width:42px">Short note on this point.</div>
  <div class="pill" style="left:232px;top:75px;width:42px;background:var(--blue)">Healthy</div>
  <div class="note" style="left:232px;top:83px;width:42px">Short note on this point.</div>
  <div class="abs" style="left:12px;top:123px;width:264px;display:grid;grid-template-columns:repeat(4,1fr);gap:2px">
    <div><div class="pill" style="position:static;border-radius:1px;background:var(--blue)">Industry</div><div class="note" style="position:static;background:#f1f2f4;padding:1px">Short note here.</div></div>
    <div><div class="pill" style="position:static;border-radius:1px;background:var(--yellow)">Investment</div><div class="note" style="position:static;background:#f1f2f4;padding:1px">Short note here.</div></div>
    <div><div class="pill" style="position:static;border-radius:1px;background:var(--navy)">Ecology</div><div class="note" style="position:static;background:#f1f2f4;padding:1px">Short note here.</div></div>
    <div><div class="pill" style="position:static;border-radius:1px;background:var(--blue)">Healthy</div><div class="note" style="position:static;background:#f1f2f4;padding:1px">Short note here.</div></div>
  </div>
  <div class="foot"></div><div class="tag">Vemtra</div>
</section>

<!-- Row 4 -->
<section class="slide c1 r4">
  <div class="ttl">USA Map</div>
  <div class="photo" role="img" aria-label="Grey map of the United States with location pins" style="left:80px;top:36px;width:130px;height:86px;background:radial-gradient(ellipse,#c9cdd2,#e7e9ec 70%,#fff)"></div>
  <div class="abs" style="left:14px;top:48px;width:10px;height:10px;border-radius:50%;border:2.5px dotted var(--blue)"></div>
  <div class="abs big" style="left:42px;top:34px;font-size:10px;color:var(--blue)">57%</div>
  <div class="pill" style="left:38px;top:47px;width:34px;background:var(--blue)">Data</div>
  <div class="note" style="left:38px;top:55px;width:34px">Short note on this point here.</div>
  <div class="abs" style="left:14px;top:114px;width:10px;height:10px;border-radius:50%;border:2.5px dotted var(--orange)"></div>
  <div class="abs big" style="left:42px;top:100px;font-size:10px;color:var(--orange)">89%</div>
  <div class="pill" style="left:38px;top:113px;width:34px;background:var(--orange)">Data</div>
  <div class="note" style="left:38px;top:121px;width:34px">Short note on this point here.</div>
  <div class="abs" style="left:222px;top:48px;width:10px;height:10px;border-radius:50%;border:2.5px dotted var(--navy)"></div>
  <div class="abs big" style="left:244px;top:34px;font-size:10px;color:var(--navy)">45%</div>
  <div class="pill" style="left:240px;top:47px;width:34px;background:var(--navy)">Data</div>
  <div class="note" style="left:240px;top:55px;width:34px">Short note on this point here.</div>
  <div class="abs" style="left:222px;top:114px;width:10px;height:10px;border-radius:50%;border:2.5px dotted var(--yellow)"></div>
  <div class="abs big" style="left:244px;top:100px;font-size:10px;color:var(--yellow)">79%</div>
  <div class="pill" style="left:240px;top:113px;width:34px;background:var(--yellow)">Data</div>
  <div class="note" style="left:240px;top:121px;width:34px">Short note on this point here.</div>
  <div class="foot"></div><div class="tag">Vemtra</div>
</section>

<section class="slide c2 r4">
  <div class="ttl">USA Map</div>
  <div class="photo" role="img" aria-label="Map of the United States with states in blue, yellow, orange and navy" style="left:14px;top:40px;width:140px;height:90px;background:linear-gradient(120deg,#2f73b6,#f2c318 35%,#f08a2c 60%,#2c3e50)"></div>
  <div class="abs" style="left:158px;top:44px;display:grid;gap:7px">
    <div style="display:flex;align-items:center;gap:4px"><span style="width:7px;height:7px;border-radius:50%;border:1.5px solid var(--blue);display:block"></span><span class="big" style="font-size:12px;color:var(--blue);width:34px">78%</span><span style="width:1px;height:14px;background:var(--blue)"></span><span class="note" style="position:static;text-align:left;width:50px">Short note on this key point here.</span></div>
    <div style="display:flex;align-items:center;gap:4px"><span style="width:7px;height:7px;border-radius:50%;border:1.5px solid var(--yellow);display:block"></span><span class="big" style="font-size:12px;color:var(--yellow);width:34px">63%</span><span style="width:1px;height:14px;background:var(--yellow)"></span><span class="note" style="position:static;text-align:left;width:50px">Short note on this key point here.</span></div>
    <div style="display:flex;align-items:center;gap:4px"><span style="width:7px;height:7px;border-radius:50%;border:1.5px solid var(--navy);display:block"></span><span class="big" style="font-size:12px;color:var(--navy);width:34px">26%</span><span style="width:1px;height:14px;background:var(--navy)"></span><span class="note" style="position:static;text-align:left;width:50px">Short note on this key point here.</span></div>
    <div style="display:flex;align-items:center;gap:4px"><span style="width:7px;height:7px;border-radius:50%;border:1.5px solid var(--orange);display:block"></span><span class="big" style="font-size:12px;color:var(--orange);width:34px">82%</span><span style="width:1px;height:14px;background:var(--orange)"></span><span class="note" style="position:static;text-align:left;width:50px">Short note on this key point here.</span></div>
  </div>
  <div class="foot"></div><div class="tag">Vemtra</div>
</section>

<section class="slide c3 r4" style="background:var(--blue)">
  <div class="photo" role="img" aria-label="Dark circuit board close-up" style="left:110px;top:0;width:178px;height:161px;border-radius:60px 0 0 60px;background:linear-gradient(130deg,#3a3f48,#6b707a 45%,#23272d)"></div>
  <div class="abs" style="left:18px;top:58px;width:90px;color:#fff">
    <div style="font-size:4px;font-weight:700;margin-bottom:6px">LOREM IPSUM DOLOR SIT AMET</div>
    <div style="font-size:3.2px;line-height:1.45">Short note on the key point for this slide goes here with a brief line of support text for the reader.</div>
  </div>
</section>

<section class="slide c4 r4">
  <div class="photo" role="img" aria-label="Dark circuit board close-up" style="left:0;top:0;width:288px;height:161px;background:linear-gradient(135deg,#2c3139,#676d77 50%,#1f2328)"></div>
  <div class="abs" style="left:0;top:14px;width:262px;height:147px;background:var(--blue);border-radius:0 60px 0 0"></div>
  <div class="abs" style="left:88px;top:70px;width:160px;color:#fff">
    <div style="font-size:5px;margin-bottom:5px">Lorem Ipsum is simply dummy Text Here</div>
    <div style="font-size:2.8px;line-height:1.45;opacity:.85;margin-bottom:6px">Short note on the key point for this slide goes here with a brief line of support text for the reader.</div>
    <div style="display:grid;grid-template-columns:1fr 1fr;gap:8px;font-size:2.6px;line-height:1.45">
      <p>Short note on the key point for this slide goes here with support text.</p>
      <p>Short note on the key point for this slide goes here with support text.</p>
    </div>
  </div>
  <div class="abs" style="left:10px;top:134px;font-size:17px;font-weight:700;color:rgba(255,255,255,.22)">Vemtra</div>
</section>

<!-- Row 5 -->
<section class="slide c1 r5" style="background:#3a4450">
  <div class="photo" role="img" aria-label="Office workspace photograph" style="left:0;top:0;width:288px;height:161px;background:linear-gradient(120deg,#6a727c,#a4abb3 55%,#4c535c)"></div>
  <div class="abs" style="left:0;top:0;width:230px;height:161px;background:var(--blue);clip-path:polygon(0 0,100% 0,82% 100%,0 100%)"></div>
  <div class="abs" style="left:14px;top:18px;width:190px;color:#fff">
    <div style="display:flex;gap:5px;align-items:flex-start">
      <span style="font-size:20px;font-weight:900;line-height:.9">“</span>
      <p style="font-size:8.5px;line-height:1.2">We are on mission to revolution the hospitality industry with our innovative model and technology platform.</p>
    </div>
    <p style="font-size:3.2px;line-height:1.5;margin-top:10px">Short note on the key point for this slide goes here with a brief line of support text for the reader and the room around it.</p>
    <div style="margin:10px 0 0 110px;width:34px;height:5px;border-radius:3px;background:#fff;color:var(--blue);font-size:2.6px;text-align:center;line-height:5px">LOREM IPSUM</div>
  </div>
</section>

<section class="slide c2 r5">
  <div class="photo" role="img" aria-label="Chip on a blue hexagon circuit pattern" style="left:0;top:10px;width:100px;height:146px;background:linear-gradient(160deg,#6aa6d4,#9cc8e6 50%,#d49a45 62%,#6aa6d4)"></div>
  <div class="abs" style="left:104px;top:22px;font-size:8.5px;color:var(--blue)">LOREM IPSUM DOLOR SIT AMET</div>
  <div class="abs fine" style="left:104px;top:36px;width:160px">Short note on the key point for this slide goes here with a brief line of support text for the reader and the room.</div>
  <div class="abs" style="left:144px;top:96px;font-size:12px;color:var(--blue)">01</div>
  <div class="abs" style="left:164px;top:96px;width:80px"><div style="font-size:4px;color:var(--blue)">Content Title #01</div><div class="fine">Short note on the key point for this slide here.</div></div>
  <div class="abs" style="left:144px;top:128px;font-size:12px;color:var(--orange)">02</div>
  <div class="abs" style="left:164px;top:128px;width:80px"><div style="font-size:4px;color:var(--orange)">Content Title #02</div><div class="fine">Short note on the key point for this slide here.</div></div>
  <div class="foot"></div><div class="tag">Vemtra</div>
</section>

<section class="slide c3 r5">
  <div class="abs" style="left:0;top:20px;width:122px;height:141px;background:var(--orange);border-radius:0 0 70px 0"></div>
  <div class="photo" role="img" aria-label="Chip on a blue hexagon circuit pattern" style="left:0;top:10px;width:118px;height:136px;border-radius:0 0 68px 0;background:linear-gradient(150deg,#6aa6d4,#9cc8e6 45%,#d49a45 58%,#6aa6d4)"></div>
  <div class="abs" style="left:132px;top:20px;font-size:8.5px;color:var(--blue)">Lorem ipsum dolor sit amet</div>
  <div class="abs fine" style="left:132px;top:34px;width:140px">Short note on the key point for this slide goes here with a brief line of support text for the reader.</div>
  <div class="abs" style="left:142px;top:66px;display:flex;gap:4px;width:130px"><span style="flex:none;width:10px;height:10px;border-radius:50%;background:var(--orange)"></span><div><div style="font-size:4px;color:var(--blue)">Content Title #01</div><div class="fine">Short note on the key point for this slide.</div></div></div>
  <div class="abs" style="left:156px;top:96px;display:flex;gap:4px;width:120px"><span style="flex:none;width:10px;height:10px;border-radius:50%;background:var(--orange)"></span><div><div style="font-size:4px;color:var(--blue)">Content Title #02</div><div class="fine">Short note on the key point for this slide.</div></div></div>
  <div class="abs" style="left:132px;top:126px;display:flex;gap:4px;width:130px"><span style="flex:none;width:10px;height:10px;border-radius:50%;background:var(--orange)"></span><div><div style="font-size:4px;color:var(--blue)">Content Title #03</div><div class="fine">Short note on the key point for this slide.</div></div></div>
  <div class="foot"></div><div class="tag">Vemtra</div>
</section>

<section class="slide c4 r5">
  <div class="abs" style="left:18px;top:12px;font-size:10px;font-weight:700;color:var(--blue)">TABLE</div>
  <div class="abs" style="left:18px;top:25px;font-size:3px;color:var(--soft)">Type the subtitle of your great here</div>
  <div class="abs" style="left:18px;top:52px;width:252px">
    <div style="font-size:3.4px;color:var(--blue);font-weight:700">Your title here</div>
    <div class="fine">Short note on the key point for this slide goes here with a brief line of support text for the reader and the room around it, kept clear and simple.</div>
  </div>
  <div class="abs" style="left:18px;top:80px;width:252px">
    <table class="grid">
      <tr><th>Name</th><th>Section A</th><th>Section B</th><th>Section C</th><th>Section D</th><th>Section E</th><th>Section F</th><th>Section G</th><th>Section H</th></tr>
      <tr><td>Section 01</td><td>1305</td><td>1305</td><td>1305</td><td>1305</td><td>1305</td><td>1305</td><td>1305</td><td>1305</td></tr>
      <tr><td>Section 02</td><td>515</td><td>515</td><td>515</td><td>515</td><td>515</td><td>515</td><td>515</td><td>515</td></tr>
      <tr><td>Section 03</td><td>765</td><td>765</td><td>765</td><td>765</td><td>765</td><td>765</td><td>765</td><td>765</td></tr>
      <tr><td>Section 04</td><td>865</td><td>865</td><td>865</td><td>865</td><td>865</td><td>865</td><td>865</td><td>865</td></tr>
    </table>
  </div>
  <div class="foot"></div><div class="tag">Vemtra</div>
</section>

<!-- Row 6 -->
<section class="slide c1 r6">
  <div class="ttl" style="font-weight:400;letter-spacing:-.2px">Process / Bullet Points</div>
  <p class="abs" style="left:14px;top:58px;width:82px;font-size:6.2px;line-height:1.3;color:var(--ink)">Lorem ipsum dolor sit amet, consectetuer adipiscing elit. Aenean commodo ligula eget dolor</p>
  <div class="abs" style="left:110px;top:46px;width:26px;height:26px;border-radius:50%;background:var(--blue)"></div>
  <div class="abs" style="left:161px;top:46px;width:26px;height:26px;border-radius:50%;background:var(--orange)"></div>
  <div class="abs" style="left:212px;top:46px;width:26px;height:26px;border-radius:50%;background:var(--navy)"></div>
  <div class="abs" style="left:117px;top:53px;width:12px;height:12px;border-radius:50%;border:1.5px solid #fff"></div>
  <div class="abs" style="left:168px;top:53px;width:12px;height:12px;border-radius:50%;border:1.5px solid #fff"></div>
  <div class="abs" style="left:219px;top:53px;width:12px;height:12px;border-radius:50%;border:1.5px solid #fff"></div>
  <div class="abs" style="left:141px;top:56px;font-size:6px;color:#888">→</div>
  <div class="abs" style="left:192px;top:56px;font-size:6px;color:#888">→</div>
  <div class="abs" style="left:110px;top:84px;width:46px"><div style="font-size:4px;color:#666">Analysis</div><div class="fine">Short note on the key point for this slide here.</div></div>
  <div class="abs" style="left:161px;top:84px;width:46px"><div style="font-size:4px;color:#666">Evaluate</div><div class="fine">Short note on the key point for this slide here.</div></div>
  <div class="abs" style="left:212px;top:84px;width:46px"><div style="font-size:4px;color:#666">Profit</div><div class="fine">Short note on the key point for this slide here.</div></div>
  <div class="foot"></div><div class="tag">Vemtra</div>
</section>

<section class="slide c2 r6">
  <div class="ttl" style="top:6px;font-weight:400;font-size:9px">Pricing Table</div>
  <p class="abs" style="left:40px;top:21px;width:208px;text-align:center;font-size:6.4px;line-height:1.2">Lorem ipsum dolor sit amet, consectetuer adipiscing elit. Aenean commodo ligula eget dolor.</p>
  <div class="card" style="left:34px;top:50px;width:68px;height:105px">
    <div class="rec" style="background:var(--blue)">RECOMMENDED</div><div class="pkg" style="color:var(--blue)">Package One</div><div class="price">$9/Month</div>
    <ul><li>5000+ Core Slides*</li><li>Free Support</li><li>Lifetime Updates</li><li>One-off Payment</li><li>28k Exclusive Icons</li><li>Pre-made Slides</li></ul>
    <div class="try" style="background:var(--blue)">TRY NOW</div>
  </div>
  <div class="card" style="left:110px;top:50px;width:68px;height:105px">
    <div class="rec" style="background:var(--orange)">RECOMMENDED</div><div class="pkg" style="color:var(--orange)">Package One</div><div class="price">$9/Month</div>
    <ul><li>5000+ Core Slides*</li><li>Free Support</li><li>Lifetime Updates</li><li>One-off Payment</li><li>28k Exclusive Icons</li><li>Pre-made Slides</li></ul>
    <div class="try" style="background:var(--orange)">TRY NOW</div>
  </div>
  <div class="card" style="left:186px;top:50px;width:68px;height:105px">
    <div class="rec" style="background:var(--navy)">RECOMMENDED</div><div class="pkg" style="color:var(--navy)">Package One</div><div class="price">$9/Month</div>
    <ul><li>5000+ Core Slides*</li><li>Free Support</li><li>Lifetime Updates</li><li>One-off Payment</li><li>28k Exclusive Icons</li><li>Pre-made Slides</li></ul>
    <div class="try" style="background:var(--navy)">TRY NOW</div>
  </div>
  <div class="foot"></div><div class="tag">Vemtra</div>
</section>

<section class="slide c3 r6">
  <div class="ttl" style="font-weight:400;font-size:6px">Pricing Table</div>
  <div class="card" style="left:18px;top:42px;width:54px;height:110px">
    <div class="rec" style="background:var(--navy)">RECOMMENDED</div><div class="pkg">Package One</div><div class="price">$9/Month</div>
    <ul><li>5000+ Core Slides*</li><li>Free Support</li><li>Lifetime Updates</li><li>One-off Payment</li><li>Lorem ipsum dolor</li><li>Lorem ipsum dolor</li><li>Lorem ipsum dolor</li></ul>
  </div>
  <div class="card" style="left:74px;top:30px;width:54px;height:126px;z-index:1">
    <div class="rec" style="background:var(--blue)">RECOMMENDED</div><div class="pkg" style="color:var(--blue)">Package One</div><div class="price" style="color:var(--blue)">$9/Month</div>
    <ul><li>Lorem ipsum dolor</li><li>Free Support</li><li>Lifetime Updates</li><li>Lorem ipsum dolor</li><li>Lorem ipsum dolor</li><li>Lorem ipsum dolor</li><li>Lorem ipsum dolor</li><li>Lorem ipsum dolor</li></ul>
    <div class="try" style="background:var(--blue)">TRY NOW</div>
  </div>
  <div class="card" style="left:130px;top:42px;width:54px;height:110px">
    <div class="rec" style="background:var(--navy)">RECOMMENDED</div><div class="pkg">Package One</div><div class="price">$9/Month</div>
    <ul><li>Lorem ipsum dolor</li><li>Free Support</li><li>Lifetime Updates</li><li>One-off Payment</li><li>Lorem ipsum dolor</li><li>Lorem ipsum dolor</li><li>Lorem ipsum dolor</li></ul>
  </div>
  <div class="abs" style="left:196px;top:44px;width:80px;display:grid;gap:5px">
    <div style="display:flex;gap:3px"><span style="flex:none;width:6px;height:6px;border-radius:50%;background:var(--orange)"></span><div style="font-size:3.2px;color:#555">The Beginning<div class="fine">Short note on this step here.</div></div></div>
    <div style="display:flex;gap:3px"><span style="flex:none;width:6px;height:6px;border-radius:50%;background:var(--orange)"></span><div style="font-size:3.2px;color:#555">The Struggle<div class="fine">Short note on this step here.</div></div></div>
    <div style="display:flex;gap:3px"><span style="flex:none;width:6px;height:6px;border-radius:50%;background:var(--orange)"></span><div style="font-size:3.2px;color:#555">The Struggle<div class="fine">Short note on this step here.</div></div></div>
    <div style="display:flex;gap:3px"><span style="flex:none;width:6px;height:6px;border-radius:50%;background:var(--orange)"></span><div style="font-size:3.2px;color:#555">The Finishing<div class="fine">Short note on this step here.</div></div></div>
    <div style="display:flex;gap:3px"><span style="flex:none;width:6px;height:6px;border-radius:50%;background:var(--orange)"></span><div style="font-size:3.2px;color:#555">The Winning<div class="fine">Short note on this step here.</div></div></div>
  </div>
  <div class="foot"></div><div class="tag">Vemtra</div>
</section>

<section class="slide c4 r6">
  <div class="ttl" style="top:12px;font-weight:300;font-size:8.5px;letter-spacing:-.3px">Lorem ipsum dolor sit amet</div>
  <div class="abs" style="left:18px;top:48px;width:254px;display:grid;grid-template-columns:repeat(4,1fr);gap:10px">
    <div><div style="font-size:4px;color:#555">Lorem<br>ipsum</div><div class="fine" style="margin-top:3px">Short note on the key point for this slide here.</div></div>
    <div><div style="font-size:4px;color:#555">Lorem<br>ipsum</div><div class="fine" style="margin-top:3px">Short note on the key point for this slide here.</div></div>
    <div><div style="font-size:4px;color:#555">Lorem<br>ipsum</div><div class="fine" style="margin-top:3px">Short note on the key point for this slide here.</div></div>
    <div><div style="font-size:4px;color:#555">Lorem<br>ipsum</div><div class="fine" style="margin-top:3px">Short note on the key point for this slide here.</div></div>
  </div>
  <div class="photo" role="img" aria-label="Team stacking hands together" style="left:18px;top:96px;width:98px;height:44px;background:linear-gradient(120deg,#c9ced4,#eceef0 50%,#a8b0b8)"></div>
  <div class="abs" style="left:116px;top:96px;width:52px;height:44px;background:var(--orange)">
    <svg width="52" height="44" viewBox="0 0 52 44"><rect x="18" y="13" width="16" height="16" rx="1" fill="none" stroke="#fff" stroke-width="1.4"/><line x1="18" y1="18" x2="34" y2="18" stroke="#fff" stroke-width="1.2"/><line x1="22" y1="11" x2="22" y2="15" stroke="#fff" stroke-width="1.2"/><line x1="30" y1="11" x2="30" y2="15" stroke="#fff" stroke-width="1.2"/></svg>
  </div>
  <div class="abs" style="left:168px;top:96px;width:104px;height:44px;background:#eceef0;display:flex;align-items:center;gap:6px;padding-left:8px">
    <span style="font-size:15px;font-weight:300;color:#777">85%</span>
    <span class="fine" style="width:44px">Short note on the key point here.</span>
  </div>
  <div class="foot"></div><div class="tag">Vemtra</div>
</section>

</body>
</html>
```